Pitch book for Birchmere Property Partners.

Birchmere Partners is a new real estate investment company focused on multifamily (apartment) investments along the San Francisco Peninsula (in other parts of the world it is also referred to as flats). We need a professional Pitch Book i.e. brochure (digital and print) to raise equity from private investors. Read about “pitch book” on Lexipedia. The profile of the investor is conservative and must qualify as an accredited investor. Think high net worth individuals, CEOs and wealthy retiring couples. The investor that is attracted to real estate invest because it is low risk, produce cash flow and provide solid returns over the long term.

The brochure should convey trust, be highly professional and be clean and crisp. I attach a PowerPoint doc to be used as a copy for the brochure. I also attach a brochure of Halvert Crane – I like the look and feel, think it was designed with InDesign.

We will use the brochure at one-on-one meetings with investors where we will present on a laptop; we also need it in a format so that we can email it, print it and use it to be uploaded as a website.

I prefer the up and down scroll format (like you would do on a Mac) compared to PowerPoint but I am open to suggestions.

The photos I used in the PowerPoint presentation was found on the web, please use your own stock images.

Target Market(s)

High net worth individuals

Industry/Entity Type

Real Estate

Font styles to use
Serif

Requirements
Must have
• See attached Power Point
Nice to have
• See attached HVC brochure, I like the look and feel.
Should not have
• I am open to your ideas.

```html
<!DOCTYPE html>
<html lang="en">
<head>
<meta charset="utf-8">
<title>Birchmere Partners — Pitch Book Cover</title>
<link rel="stylesheet" href="https://fonts.googleapis.com/css2?family=Open+Sans:wght@400;600;700&display=swap">
<style>
  :root {
    --backdrop: #d6d6d4;
    --cover-grey: #5e5d5d;
    --ink-light: #ffffff;
    --ink-soft: #e4e4e4;
    --sky-top: #8fb0d0;
    --sky-mid: #aac3db;
    --glass-dark: #1d2128;
    --glass-mid: #4a5566;
    --stone: #c9c2b0;
  }
  * { box-sizing: border-box; margin: 0; padding: 0; }
  html, body {
    width: 1200px; height: 800px; overflow: hidden;
    background: var(--backdrop);
    font-family: "Open Sans", Arial, sans-serif;
  }
  .spread {
    position: absolute; left: 130px; top: 70px;
    width: 940px; height: 660px;
    display: flex;
    box-shadow: 0 6px 18px rgba(0,0,0,0.18);
  }
  .back-cover {
    position: relative; width: 470px; height: 100%;
    background: var(--cover-grey);
    color: var(--ink-light);
  }
  .front-cover {
    position: relative; width: 470px; height: 100%;
    overflow: hidden;
  }
  .cover-photo {
    position: absolute; inset: 0;
    background:
      linear-gradient(115deg, transparent 0 22%, var(--glass-dark) 22% 30%, transparent 30%),
      linear-gradient(100deg, transparent 0 36%, var(--glass-mid) 36% 62%, var(--glass-dark) 62% 80%, var(--stone) 80% 86%, var(--glass-mid) 86%),
      linear-gradient(180deg, var(--sky-top), var(--sky-mid));
  }
  .brand {
    display: flex; flex-direction: column; align-items: center; gap: 8px;
  }
  .brand-mark {
    width: 34px; height: 34px; border-radius: 50%;
    background: var(--ink-light);
  }
  .brand-name {
    font-size: 15px; font-weight: 600; letter-spacing: 0.08em;
    color: var(--ink-light);
  }
  .back-cover .brand {
    position: absolute; left: 0; right: 0; top: 430px;
  }
  .contacts {
    position: absolute; left: 0; right: 0; top: 500px;
    text-align: center; font-size: 11.5px; line-height: 1.45;
    color: var(--ink-soft);
  }
  .contact-firm { font-weight: 700; color: var(--ink-light); }
  .contact-block + .contact-block { margin-top: 2px; }
  .cover-title {
    position: absolute; right: 34px; top: 36px;
    text-align: left; color: var(--ink-light);
  }
  .cover-title h1 {
    font-size: 22px; font-weight: 600; line-height: 1.05;
  }
  .cover-title p {
    font-size: 9px; margin-top: 4px; letter-spacing: 0.02em;
  }
  .front-cover .brand {
    position: absolute; right: 60px; top: 470px;
  }
</style>
</head>
<body>
  <main class="spread">
    <section class="back-cover">
      <div class="brand">
        <span class="brand-mark"></span>
        <span class="brand-name">BIRCHMERE</span>
      </div>
      <address class="contacts" style="font-style:normal">
        <div class="contact-block">
          <div class="contact-firm">Birchmere Partners</div>
          <div>Noel Varga</div>
          <div>nvarga@birchmerepartners.com</div>
          <div>1.415.555.0142</div>
        </div>
        <div class="contact-block">
          <div class="contact-firm">Ashford &amp; Associates (Estate Planning)</div>
          <div>Martin Ashford</div>
          <div>martin@ashford-cpa.com</div>
          <div>650.555.0187</div>
        </div>
      </address>
    </section>
    <section class="front-cover">
      <div class="cover-photo" role="img" aria-label="Upward view of glass office towers against a blue, cloudy sky"></div>
      <div class="cover-title">
        <h1>San Francisco<br>Peninsula</h1>
        <p>Multifamily Real Estate Investment</p>
      </div>
      <div class="brand">
        <span class="brand-mark"></span>
        <span class="brand-name">BIRCHMERE</span>
      </div>
    </section>
  </main>
</body>
</html>
```